Redesign of an app landing page

Our page zemrik.net needs a redesign. This would follow the typical app landing page format which we have now, that is to say a single page with some text, pictures etc. There is also a link to a seperate page with a facebook privacy policy that could use a quick polish.

I want to page to keep the minimamlistic feel that it has now but simply with a better design, a picture that fits the whole screen and the text area similar. You are free to use your design abilities to go outside this preferences if you feel the need to.

The picture in the background should show a social situation which could be anything from taking a lunch, go running, to a museum, the movies, party (no alcohol) or any other situation that we do with our friends. Our logo should be visible as well. If you need any more information, don“t hesitate to take contact

Examples of pages that I like

https://www.lumtavo.example/

http://kradlefin.example/

http://vostrel.example/

Number of Pages Required

1 page

Colors
00a990
0292cd

Requirements
Must have
• The following links need to be there with the correct logos for the pages and the download button should the most visible
• Facebook #community
• Instagram: #gallery
• Play store: #download
• There needs to be as well the facebook privacy policy link but this can be in small letters somewhere in the corner like it is now.
• #privacy

```html
<!DOCTYPE html>
<html lang="en">
<head>
<meta charset="utf-8">
<title>Zemrik – Connect with like-minded people</title>
<link rel="stylesheet" href="https://fonts.googleapis.com/css2?family=Comfortaa:wght@700&family=Raleway:wght@400;500&display=swap">
<style>
  :root {
    --brand: #33b2cc;
    --brand-dark: #2895ad;
    --text-light: #ffffff;
    --band: rgba(40, 36, 38, 0.72);
    --photo-warm: #e9b7a8;
    --photo-dark: #1a0f12;
    --panel: #0d0a0b;
    --divider: rgba(255, 255, 255, 0.35);
  }
  * { box-sizing: border-box; margin: 0; padding: 0; }
  html, body { width: 1200px; height: 658px; overflow: hidden; background: var(--photo-dark); }
  body { font-family: "Raleway", sans-serif; color: var(--text-light); }

  .landing { position: relative; width: 1200px; height: 658px; overflow: hidden; }

  .hero-photo {
    position: absolute; inset: 0;
    background:
      radial-gradient(ellipse 360px 220px at 430px 80px, #fbe9d8 0%, rgba(246,205,180,0.75) 40%, transparent 100%),
      radial-gradient(circle 70px at 140px 160px, rgba(255,240,245,0.8), transparent),
      radial-gradient(ellipse 300px 200px at 120px 120px, rgba(200,110,130,0.7), transparent),
      linear-gradient(180deg, var(--photo-warm) 0%, #8c5a5a 38%, #3a2226 62%, var(--photo-dark) 100%);
  }

  .info-band {
    position: absolute; left: 0; top: 292px; width: 670px; height: 108px;
    background: var(--band);
  }

  .feature-panel {
    position: absolute; left: 648px; top: 18px; width: 560px; height: 610px;
    background: var(--panel); opacity: 0.82;
    clip-path: polygon(30% 6%, 95% 0%, 100% 30%, 100% 85%, 68% 100%, 18% 94%, 0% 47%);
  }

  .download-button {
    position: absolute; left: 135px; top: 328px; width: 224px; height: 38px;
    display: flex; border-radius: 3px; overflow: hidden; text-decoration: none;
    background: var(--brand); color: var(--text-light);
  }
  .download-button__label {
    flex: 1; display: flex; align-items: center; justify-content: center;
    font-size: 15.5px; font-weight: 400; letter-spacing: 0.2px;
  }
  .download-button__icon {
    width: 38px; display: flex; align-items: center; justify-content: center;
    background: var(--brand-dark);
  }

  .social-links {
    position: absolute; left: 431px; top: 333px; height: 30px;
    display: flex; align-items: center;
  }
  .social-links__icon {
    width: 30px; height: 30px; border-radius: 50%;
    border: 2px solid var(--text-light); margin-right: 11px;
  }
  .social-links .divider { width: 1px; height: 20px; background: var(--divider); margin: 0 19px 0 10px; }
  .social-links__privacy { color: var(--text-light); text-decoration: none; font-size: 14px; }

  .copyright {
    position: absolute; left: 242px; top: 415px; font-size: 15px; white-space: nowrap;
  }

  .brand {
    position: absolute; right: 122px; top: 96px;
    display: flex; flex-direction: column; align-items: flex-end;
  }
  .brand__mark {
    width: 104px; height: 104px; border-radius: 18px;
    background: linear-gradient(135deg, #7fcfe0, var(--brand));
  }
  .brand__name {
    margin-top: 8px; font-family: "Raleway", sans-serif; font-weight: 500;
    font-size: 42px; line-height: 1; color: var(--brand);
  }

  .welcome {
    position: absolute; right: 120px; top: 270px; width: 420px; text-align: right;
  }
  .welcome__title {
    font-family: "Comfortaa", sans-serif; font-weight: 700; font-size: 25px;
    line-height: 30px; color: var(--brand); margin-bottom: 18px;
  }
  .welcome__text { font-size: 15px; line-height: 26.6px; }
</style>
</head>
<body>
<main class="landing">
  <div class="hero-photo" role="img" aria-label="Concert crowd with raised hands under warm stage lights"></div>

  <div class="feature-panel"></div>

  <div class="info-band"></div>

  <a class="download-button" href="#download">
    <span class="download-button__label">DOWNLOAD ZEMRIK</span>
    <span class="download-button__icon">
      <svg width="20" height="20" viewBox="0 0 20 20" fill="none" stroke="#fff" stroke-width="2.4" stroke-linecap="square">
        <path d="M10 2v10M6 8l4 4 4-4"/>
        <path d="M2 13v5h16v-5"/>
      </svg>
    </span>
  </a>

  <nav class="social-links">
    <a class="social-links__icon" href="#community" aria-label="Community page"></a>
    <a class="social-links__icon" href="#gallery" aria-label="Photo page"></a>
    <span class="divider"></span>
    <a class="social-links__privacy" href="#privacy">Privacy Policy</a>
  </nav>

  <p class="copyright">Copyright 2015 Zemrik. All rights reserved.</p>

  <div class="brand">
    <div class="brand__mark"></div>
    <div class="brand__name">zemrik</div>
  </div>

  <section class="welcome">
    <h1 class="welcome__title">Welcome to zemrik</h1>
    <p class="welcome__text">Zemrik is a free app that connect you<br>with new people and allows you to grow your<br>social network. Zemrik lets you publish<br>any activity you want to the community and<br>connect with like-minded people. You<br>can also browse through posted<br>activities andjoin the ones you like.</p>
  </section>
</main>
</body>
</html>
```